lumo - relief chair needs new website

New swiss made chair to relief back pain needs professional web design.
lumo is the brand name for a new swiss product. Developed and build in Switzerland.
The main value for customers is back pain relief.

IA - Home, Product, Testimonials, Consulting, Where to buy, Contact

We like to see light gray, white and green as the main colors.
modern, clean design, user centered view, parallax scrolling, MUST be responsive
The design should transfer trust and value toward potential customers.

Add info:

Headlines:
lumo - entlastet - entspannt - befreit
- Volkskrankheit: Rückenschmerzen

You can find more information about the product on the website for the developing company. www.tarvenko.ch.

As we from marketing decided to build a new brand around this chair we re-branded the product "lumo" and starting to set-up everything new.

Please ask if you have questions

Adress:
lumo - Entlastungsstuhl
Kornweidweg 42
6217 Schweiz

Tel: +41 52 318 26 41
Fax: +41 52 318 26 58

E-Mail: info@lumo-??.ch

Target Market(s)

Switzerland, Germany, Austria

Industry/Entity Type

Health Care

Number of Pages Required

5+ page

Font styles to use
Sans Serif

Requirements
Must have
• Responsive
• parallax scrolling (on website)
• Designer has to deliver photoshop or illustrator files (incl. layer) for pages as our programmer will adapt design to our CMS system

```html
<!DOCTYPE html>
<html lang="de">
<head>
<meta charset="utf-8">
<title>lumo - Entlastungsstuhl</title>
<link rel="stylesheet" href="https://fonts.googleapis.com/css2?family=Open+Sans:ital,wght@0,400;0,600;0,700;1,400&family=Crimson+Text:wght@600&display=swap">
<style>
:root{
  --green:#4caf50;
  --green-dark:#3d9a40;
  --heading:#666666;
  --text:#8a8a8a;
  --text-dark:#444444;
  --light:#f5f5f5;
  --white:#ffffff;
  --field:#15181d;
}
*{margin:0;padding:0;box-sizing:border-box}
html,body{width:1200px;height:3051px;overflow:hidden}
body{position:relative;font-family:"Open Sans",Arial,sans-serif;background:var(--white);color:var(--text)}
.abs{position:absolute}
.site-header{left:0;top:0;width:1200px;height:69px;background:var(--white)}
.brand{left:72px;top:10px;display:flex;align-items:center;gap:8px}
.brand-mark{width:26px;height:26px;border-radius:50%;background:var(--green)}
.brand-name{font-weight:700;font-size:30px;color:var(--green);line-height:1}
.nav a{position:absolute;top:20px;font-size:15px;color:#333;text-decoration:none;line-height:30px}
.nav .active{background:var(--green);color:#fff;padding:0 18px;border-radius:2px}
.hero{left:0;top:69px;width:1200px;height:609px;background:linear-gradient(120deg,#2a2c33 0%,#4a4d55 40%,#2f3138 70%,#1a1b1f 100%)}
.hero-welcome{left:0;width:1200px;top:288px;text-align:center;font-family:"Crimson Text",Georgia,serif;font-weight:600;font-size:37px;line-height:1.2;color:#fff}
.hero-title{left:0;width:1200px;top:355px;text-align:center;font-weight:600;font-size:39px;line-height:1.2;letter-spacing:1.5px;color:#fff}
.hero-sub{left:0;width:1200px;top:425px;text-align:center;font-size:18px;line-height:26px;color:#fff}
.hero-rule{top:438px;height:1px;width:130px;background:rgba(255,255,255,.7)}
.dots{display:flex;gap:14px;align-items:center}
.dot{width:10px;height:10px;border-radius:50%;background:#999}
.dot.on{width:14px;height:14px;background:var(--green);border:3px solid #777}
.h2{font-weight:700;font-size:38px;color:var(--heading);letter-spacing:.5px}
.h2.light{color:#fff}
.rule{width:52px;height:3px;background:var(--green)}
.rule.light{background:#fff}
.copy{font-size:12.5px;line-height:26px;color:var(--text)}
.btn{background:var(--green);color:#fff;font-size:12.5px;text-align:center;line-height:44px;border-radius:2px;box-shadow:0 3px 0 var(--green-dark)}
.photo{background:linear-gradient(160deg,#e9e6e2,#c9a77a 55%,#3b3b3b)}
.testimonials{left:0;top:1124px;width:1200px;height:394px;background:linear-gradient(110deg,#2b3140,#151924 55%,#252a34)}
.avatar{left:175px;top:1285px;width:114px;height:114px;border-radius:50%;background:linear-gradient(160deg,#d9cfc4,#8d6d5a);border:3px solid #fff}
.quote{left:323px;top:1284px;width:706px;font-style:italic;font-size:11.5px;line-height:28px;color:#fff}
.consulting{left:0;top:1518px;width:1200px;height:646px;background:var(--light)}
.list{left:96px;top:1808px;width:722px;font-size:12.5px;line-height:26px;color:var(--text-dark)}
.list p{margin-bottom:24px}
.seller{font-weight:700;color:#999;line-height:1}
.contact{left:0;top:2461px;width:1200px;height:533px;background:linear-gradient(120deg,#2a2c30,#3c3a36 40%,#24262a 80%)}
.map{left:73px;top:2634px;width:305px;height:303px;background:#efe6cf;border:4px solid #fff}
.icon-circle{width:48px;height:48px;border-radius:50%;background:#fff;display:flex;align-items:center;justify-content:center}
.info{font-size:14.5px;line-height:26px;color:#fff}
.field{background:var(--field);color:#777;font-style:italic;font-size:12px;padding:12px 16px;opacity:.9}
.footer{left:0;top:2994px;width:1200px;height:57px;background:var(--white);font-size:12px;color:#777}
</style>
</head>
<body>

<header class="abs site-header">
  <div class="abs brand"><span class="brand-mark"></span><span class="brand-name">lumo</span></div>
  <nav class="nav">
    <a class="active" style="left:405px">Home</a>
    <a style="left:515px">Product</a>
    <a style="left:618px">Testimonials</a>
    <a style="left:753px">Consulting</a>
    <a style="left:876px">Where to buy</a>
    <a style="left:1017px">Contact</a>
  </nav>
  <svg class="abs" style="left:1096px;top:22px" width="22" height="22" viewBox="0 0 22 22"><circle cx="9" cy="9" r="6.5" fill="none" stroke="#555" stroke-width="2"/><line x1="14" y1="14" x2="20" y2="20" stroke="#555" stroke-width="2.2"/></svg>
</header>

<section class="abs hero" role="img" aria-label="Photo of a woman seated in the relief chair holding its remote control"></section>
<div class="abs hero-welcome">Welcome to lumo</div>
<h1 class="abs hero-title">VOLKSKRANKHEIT: RÜCKENSCHMERZEN</h1>
<div class="abs hero-rule" style="left:307px"></div>
<div class="abs hero-sub">Lorem Ipsum is simply dummy</div>
<div class="abs hero-rule" style="left:757px"></div>
<div class="abs dots" style="left:570px;top:590px"><span class="dot"></span><span class="dot on"></span><span class="dot"></span></div>

<h2 class="abs h2" style="left:72px;top:714px">ABOUT US.</h2>
<div class="abs rule" style="left:72px;top:794px"></div>
<p class="abs copy" style="left:72px;top:826px;width:505px">Lorem Ipsum is simply dummy text of the printing and typesetting industry. Lorem Ipsum has been the industry's standard dummy text ever since the 1500s, when an unknown printer took a galley of type and scrambled it to make a type specimen book. It has survived not only five centuries, but also the leap into electronic typesetting, remaining essentially unchanged. It was popularised in the 1960s with the release of Letterfold sheets containing Lorem Ipsum passages, and more recently with desktop publishing software like Pageform Studio including versions of Lorem Ipsum.</p>
<div class="abs btn" style="left:72px;top:1044px;width:102px">Read More</div>

<h2 class="abs h2" style="left:627px;top:714px">PRODUCT.</h2>
<div class="abs rule" style="left:627px;top:794px"></div>
<div class="abs photo" style="left:630px;top:834px;width:178px;height:238px;border:4px solid #eee" role="img" aria-label="Product photo of the wooden relief chair with black cushions"></div>
<p class="abs copy" style="left:838px;top:826px;width:295px">Lorem Ipsum is simply dummy text of the printing and typesetting industry. Lorem Ipsum has been the industry's standard dummy text ever since the 1500s, when an unknown printer took a galley of type and scrambled it to make a type specimen book. It has survived not only five centuries, but also the leap into electronic.</p>
<div class="abs btn" style="left:838px;top:1044px;width:102px">Read More</div>

<section class="abs testimonials" role="img" aria-label="Dimmed background photo of a desk with notebooks and a laptop"></section>
<h2 class="abs h2 light" style="left:69px;top:1154px">TESTIMONIALS.</h2>
<div class="abs rule light" style="left:72px;top:1236px"></div>
<div class="abs avatar" role="img" aria-label="Portrait of the customer giving the testimonial"></div>
<p class="abs quote">Lorem Ipsum is simply dummy text of the printing and typesetting industry. Lorem Ipsum has been the industry's standard dummy text ever since the 1500s, when an unknown printer took a galley of type and scrambled it to make a type specimen book. It has survived not only five centuries, but also the leap into electronic typesetting, remaining essentially unchanged. It was popularised in the 1960s with the release...</p>
<div class="abs" style="left:541px;top:1398px;font-weight:600;font-size:14px;color:#fff">Miss. Lena Arvid</div>
<div class="abs" style="left:541px;top:1423px;font-style:italic;font-size:11.5px;color:#ddd">CEO, Company Name</div>
<div class="abs dots" style="left:572px;top:1478px"><span class="dot"></span><span class="dot on"></span><span class="dot"></span></div>

<section class="abs consulting"></section>
<h2 class="abs h2" style="left:70px;top:1544px">CONSULTING.</h2>
<div class="abs rule" style="left:72px;top:1626px"></div>
<p class="abs copy" style="left:72px;top:1664px;width:746px;font-size:12px;line-height:22px">Lorem Ipsum is simply dummy text of the printing and typesetting industry. Lorem Ipsum has been the industry's standard dummy text ever since the 1500s, when an unknown printer took a galley of type and scrambled it to make a type specimen book. It has survived not only five centuries, but also the leap into electronic typesetting, remaining essentially unchanged. It was popularised in the 1960s with the release of Letterfold sheets containing Lorem Ipsum passages, and more recently with desktop publishing software like Pageform Studio including versions of Lorem Ipsum.</p>
<div class="abs list">
  <p>1. It is a long established fact that a reader will be distracted by the readable content of a page when looking at its layout. The point of using Lorem Ipsum is that it has a more-or-less normal distribution of letters, as opposed.</p>
  <p>2. There are many variations of passages of Lorem Ipsum available, but the majority have suffered alteration in some form, by injected humour, or randomised words which don't look even slightly believable.</p>
  <p>3. Contrary to popular belief, Lorem Ipsum is not simply random text. It has roots in a piece of classical Latin literature from 45 BC, making it over 2000 years old.</p>
</div>
<div class="abs btn" style="left:96px;top:2050px;width:116px">Read More</div>
<div class="abs photo" style="left:857px;top:1674px;width:258px;height:415px;border:4px solid #fff;background:linear-gradient(170deg,#f3f1ef 0%,#d8c3a2 45%,#2f3340 75%,#e9e6e2 100%)" role="img" aria-label="Consultant adjusting the relief chair for a seated woman"></div>

<h2 class="abs h2" style="left:70px;top:2212px">WHERE TO BUY.</h2>
<div class="abs rule" style="left:72px;top:2293px"></div>
<div class="abs seller" style="left:73px;top:2362px;font-size:25px;color:#222">Kaufora</div>
<div class="abs seller" style="left:299px;top:2360px;font-size:28px;color:#888">Vendaro</div>
<div class="abs seller" style="left:538px;top:2357px;font-size:34px">Kartely.com</div>
<div class="abs seller" style="left:836px;top:2350px;font-size:48px">Dealvia.com</div>

<section class="abs contact" role="img" aria-label="Blurred background photo of a workspace"></section>
<h2 class="abs h2 light" style="left:70px;top:2504px">CONTACT.</h2>
<div class="abs rule light" style="left:72px;top:2584px"></div>
<div class="abs map" role="img" aria-label="Street map showing the location"></div>

<div class="abs icon-circle" style="left:434px;top:2631px">
  <svg width="24" height="24" viewBox="0 0 24 24"><path d="M12 3 2 12h3v9h5v-6h4v6h5v-9h3z" fill="var(--green)"/></svg>
</div>
<div class="abs info" style="left:502px;top:2628px">Kornweidweg 42,<br>6217 Schweiz.</div>
<div class="abs icon-circle" style="left:806px;top:2631px">
  <svg width="24" height="24" viewBox="0 0 24 24"><path d="M6.6 10.8a15 15 0 0 0 6.6 6.6l2.2-2.2a1 1 0 0 1 1-.25 11.4 11.4 0 0 0 3.6.57 1 1 0 0 1 1 1V20a1 1 0 0 1-1 1A17 17 0 0 1 3 4a1 1 0 0 1 1-1h3.5a1 1 0 0 1 1 1c0 1.25.2 2.45.57 3.57a1 1 0 0 1-.25 1z" fill="var(--green)"/></svg>
</div>
<div class="abs info" style="left:875px;top:2628px">+41 52 318 26 41<br>info@lumo-shop.ch</div>

<div class="abs field" style="left:441px;top:2717px;width:320px;height:41px">Name</div>
<div class="abs field" style="left:441px;top:2768px;width:320px;height:41px">E-Mail</div>
<div class="abs field" style="left:441px;top:2819px;width:320px;height:41px">Mobile No</div>
<div class="abs field" style="left:801px;top:2717px;width:330px;height:143px">Message</div>
<div class="abs btn" style="left:942px;top:2886px;width:189px;height:48px;line-height:48px;font-weight:600;font-size:15px;box-shadow:none">SUBMIT</div>
<svg class="abs" style="left:1158px;top:2960px" width="24" height="16" viewBox="0 0 24 16"><path d="M3 13 12 4l9 9" fill="none" stroke="#ccc" stroke-width="3"/></svg>

<footer class="abs footer">
  <div class="abs" style="left:72px;top:20px">© 2015 lumo-shop.ch</div>
  <span class="abs" style="left:1022px;top:22px;width:12px;height:12px;border-radius:50%;background:#888"></span>
  <span class="abs" style="left:1056px;top:22px;width:12px;height:12px;border-radius:50%;background:#888"></span>
  <span class="abs" style="left:1098px;top:22px;width:12px;height:12px;border-radius:50%;background:#888"></span>
  <div class="abs" style="left:1156px;top:20px;font-size:11px">C20</div>
</footer>

</body>
</html>
```